Auto glass company

THRIFTWAY
Roving Auto Glass, LLC
555-604-1973

* Windshield Replacement
* Rock Chip Repair
Danny "K"
Thriftwayrovingautoglass@mailbox-demo.net
* Fully Insured

This is what I would like on the card. The image is what I had before. Looking for a logo possible too, couldn’t find a place to add that on. It’s a auto glass company.

Target Market(s)

Auto glass

Industry/Entity Type

Auto glass

Contact Information for Business Card

Logo, business name, phone number, windshield replacement, rock chip repair, insured, owner name Danny K, email address clearvanerovingautoglass@mailbox-demo.net

Colors

Designer to choose colors to be used in the design.

Requirements
Must have
• Logo, business name, phone number, windshield replacement, rock chip repair, insured, owner name Danny K, email address clearvanerovingautoglass@mailbox-demo.net

```html
<!DOCTYPE html>
<html lang="en">
<head>
<meta charset="utf-8">
<title>Clearvane Roving Auto Glass – Business Card</title>
<link rel="stylesheet" href="https://fonts.googleapis.com/css2?family=Jost:wght@300;400;500;800&display=swap">
<style>
  :root {
    --navy: #0d2c66;
    --orange: #f6a623;
    --silver-light: #f3f4fa;
    --silver-mid: #d3d7ea;
    --silver-deep: #c4c9e3;
    --paper: #ffffff;
    --crack: #e6e9f3;
    --backdrop: #2b2b2d;
  }
  * { box-sizing: border-box; margin: 0; padding: 0; }
  html, body { width: 1200px; height: 960px; overflow: hidden; }
  body {
    background: var(--backdrop);
    font-family: "Jost", "Futura", sans-serif;
    position: relative;
  }
  .card {
    position: absolute;
    width: 720px;
    height: 411px;
    box-shadow: 0 14px 30px rgba(0,0,0,.45);
  }

  /* Front */
  .card--front {
    left: 80px; top: 50px;
    background: var(--navy);
    padding: 22px;
  }
  .card__panel {
    width: 100%; height: 100%;
    border: 4px solid var(--paper);
    background: linear-gradient(100deg, var(--silver-mid) 0%, var(--silver-light) 22%, var(--paper) 38%, var(--silver-deep) 52%, var(--silver-light) 68%, var(--paper) 100%);
    display: flex;
    flex-direction: column;
    justify-content: center;
    padding-left: 80px;
  }
  .brand__name {
    font-weight: 800;
    font-size: 92px;
    letter-spacing: 1px;
    line-height: 0.95;
    color: var(--navy);
    white-space: nowrap;
  }
  .brand__tagline {
    font-weight: 300;
    font-size: 40px;
    letter-spacing: 1px;
    color: var(--orange);
    text-transform: uppercase;
    line-height: 1.1;
    white-space: nowrap;
  }

  /* Back */
  .card--back {
    left: 400px; top: 500px;
    background: var(--paper);
    overflow: hidden;
  }
  .card__texture {
    position: absolute; inset: 0;
    background:
      radial-gradient(ellipse at 25% 30%, var(--crack) 0%, transparent 45%),
      radial-gradient(ellipse at 75% 60%, var(--crack) 0%, transparent 50%),
      radial-gradient(ellipse at 50% 90%, var(--crack) 0%, transparent 40%);
  }
  .contact {
    position: absolute; inset: 0;
    display: flex; flex-direction: column; align-items: center;
    padding-top: 56px;
  }
  .contact__name {
    font-weight: 800; font-size: 64px; line-height: 1;
    color: var(--navy); letter-spacing: 1px;
  }
  .contact__role {
    font-weight: 300; font-size: 28px; color: var(--orange);
    letter-spacing: 2px; margin-top: 2px; line-height: 1.1;
  }
  .contact__icons { margin-top: 6px; display: block; }
  .contact__phone {
    font-weight: 400; font-size: 58px; color: var(--navy);
    line-height: 1.05; margin-top: 4px;
  }
  .contact__email {
    font-weight: 400; font-size: 24px; color: var(--navy);
    line-height: 1.2; white-space: nowrap;
  }
  .services {
    margin-top: 20px;
    width: 640px;
    border-top: 2px solid var(--orange);
    border-bottom: 2px solid var(--orange);
    padding: 6px 0;
    display: flex; justify-content: center; align-items: center; gap: 8px;
    font-weight: 400; font-size: 19px; line-height: 1.2; color: var(--navy);
    text-transform: uppercase; letter-spacing: .3px;
    white-space: nowrap;
  }
  .services__tick { width: 17px; height: 17px; flex: none; }
</style>
</head>
<body>

  <section class="card card--front" aria-label="Card front">
    <div class="card__panel">
      <div class="brand__name">CLEARVANE</div>
      <div class="brand__tagline">Roving Auto Glass, LLC</div>
    </div>
  </section>

  <section class="card card--back" aria-label="Card back">
    <div class="card__texture" role="img" aria-label="Faint cracked windshield glass texture"></div>
    <div class="contact">
      <div class="contact__name">DANNY K</div>
      <div class="contact__role">OWNER</div>
      <svg class="contact__icons" width="300" height="44" viewBox="0 0 300 44" aria-hidden="true">
        <g stroke="var(--navy)" stroke-width="2">
          <line x1="20" y1="12" x2="92" y2="12"/>
          <line x1="30" y1="22" x2="92" y2="22"/>
          <line x1="40" y1="32" x2="92" y2="32"/>
          <line x1="208" y1="12" x2="280" y2="12"/>
          <line x1="208" y1="22" x2="270" y2="22"/>
          <line x1="208" y1="32" x2="260" y2="32"/>
        </g>
        <circle cx="126" cy="22" r="21" fill="var(--navy)"/>
        <circle cx="174" cy="22" r="21" fill="var(--navy)"/>
        <path d="M119 13 l4 -1 l3 6 l-3 2 q2 5 6 7 l2 -3 l6 3 l-1 4 q-10 1 -17 -18z" fill="var(--orange)"/>
        <rect x="164" y="15" width="20" height="14" rx="1.5" fill="var(--orange)"/>
        <path d="M164 16 l10 8 l10 -8" fill="none" stroke="var(--navy)" stroke-width="2"/>
      </svg>
      <div class="contact__phone">555-604-1973</div>
      <div class="contact__email">clearvanerovingautoglass@mailbox-demo.net</div>
      <div class="services">
        <span>Windshield Replacement</span>
        <svg class="services__tick" viewBox="0 0 17 17" aria-hidden="true"><rect x="1" y="3" width="13" height="13" fill="none" stroke="var(--orange)" stroke-width="2"/><path d="M4 9 l3 3 l8 -10" fill="none" stroke="var(--orange)" stroke-width="2.2"/></svg>
        <span>Rock Chip Repair</span>
        <svg class="services__tick" viewBox="0 0 17 17" aria-hidden="true"><rect x="1" y="3" width="13" height="13" fill="none" stroke="var(--orange)" stroke-width="2"/><path d="M4 9 l3 3 l8 -10" fill="none" stroke="var(--orange)" stroke-width="2.2"/></svg>
        <span>Fully Insured</span>
      </div>
    </div>
  </section>

</body>
</html>
```